Business card design needed

I need a simple business card design with contact details on one side (and a logo) and 2 logos on the other side. I would like the text to be in silver and the card black.

Target Market(s)

Luxury market

Industry/Entity Type

Business

Contact Information for Business Card

M&K Forvela, PO BOX 517, Brindlecoe, VIC, 3186

Logo Text

M&K Forvela

Requirements
Must have
• black card, 2 logos on back, M&K logo on front

Text on front should be

Neil & Priya Haverstock

Neil 0417826391 Priya 0428650147
neil@mkforvela.com priya@mkforvela.com
PO BOX 517, Brindlecoe, VIC, 3186

```html
<!DOCTYPE html>
<html lang="en">
<head>
<meta charset="utf-8">
<title>M&amp;K Forvela – Business Cards</title>
<link rel="stylesheet" href="https://fonts.googleapis.com/css2?family=Share+Tech+Mono&family=Josefin+Sans:wght@400&display=swap">
<style>
  :root {
    --paper: #ffffff;
    --sheet-edge: #8a8a8a;
    --card-edge: #3a3a3a;
    --card-black: #0b0b0b;
    --card-black-soft: #1a1a1a;
    --silver: #c9c9cc;
    --silver-light: #e6e6e8;
    --silver-dark: #9c9ca0;
  }
  html, body {
    margin: 0;
    padding: 0;
    overflow: hidden;
    background: var(--paper);
  }
  .sheet {
    position: relative;
    width: 1200px;
    height: 756px;
    box-sizing: border-box;
    border: 1px solid var(--sheet-edge);
    background: var(--paper);
    overflow: hidden;
  }
  .card {
    position: absolute;
    width: 516px;
    height: 290px;
    box-sizing: border-box;
    border: 1px solid var(--card-edge);
    background: linear-gradient(to right, var(--card-black-soft) 0%, var(--card-black) 50%, var(--card-black-soft) 100%);
    color: var(--silver);
  }
  .card--back { left: 49px; }
  .card--front { left: 625px; }
  .row-1 { top: 64px; }
  .row-2 { top: 414px; }

  /* back: partner marks */
  .partner {
    position: absolute;
    right: 21px;
    font-family: "Josefin Sans", sans-serif;
    text-align: right;
    line-height: 1;
    color: var(--silver);
  }
  .partner--eyewear {
    top: 82px;
    font-size: 12px;
    letter-spacing: 6px;
    margin-right: -6px;
  }
  .partner--eyewear .partner__name {
    display: block;
    font-size: 20px;
    letter-spacing: 2px;
    margin-right: 6px;
    margin-bottom: 9px;
    color: var(--silver-light);
  }
  .partner--house {
    top: 166px;
    display: flex;
    align-items: center;
    gap: 8px;
    font-size: 11px;
    letter-spacing: 3px;
    color: var(--silver-dark);
  }
  .partner__square {
    width: 20px;
    height: 28px;
    background: var(--silver-dark);
  }

  /* front: contact */
  .brand {
    position: absolute;
    left: 31px;
    top: 27px;
    width: 60px;
    text-align: center;
  }
  .brand__tile {
    width: 58px;
    height: 54px;
    border-radius: 7px;
    border: 1px solid var(--silver-dark);
    margin: 0 auto;
  }
  .brand__name {
    display: block;
    margin: 5px -12px 0;
    font-family: "Josefin Sans", sans-serif;
    font-size: 8px;
    white-space: nowrap;
    color: var(--silver);
  }
  .contact {
    position: absolute;
    right: 30px;
    top: 126px;
    text-align: right;
    font-family: "Share Tech Mono", monospace;
    line-height: 1;
    color: var(--silver);
  }
  .contact__name {
    margin: 0 0 14px;
    font-size: 32px;
    font-weight: 400;
    font-variant: small-caps;
    letter-spacing: 1px;
    color: var(--silver-light);
  }
  .contact__line {
    margin: 0;
    font-size: 17px;
    letter-spacing: 0.5px;
  }
  .contact__phone { margin-bottom: 8px; }
  .contact__email { text-transform: uppercase; font-size: 15px; margin-bottom: 6px; }
  .contact__address { font-size: 15px; font-variant: small-caps; }
</style>
</head>
<body>
<main class="sheet">

  <section class="card card--back row-1" aria-label="Card back">
    <div class="partner partner--eyewear">
      <span class="partner__name">VALTIER</span>EYEWEAR
    </div>
    <div class="partner partner--house">
      <span class="partner__square"></span>KELDMANN
    </div>
  </section>

  <section class="card card--front row-1" aria-label="Card front, Neil">
    <div class="brand">
      <div class="brand__tile"></div>
      <span class="brand__name">M&amp;K Forvela</span>
    </div>
    <div class="contact">
      <h2 class="contact__name">Neil Haverstock</h2>
      <p class="contact__line contact__phone">0417826391</p>
      <p class="contact__line contact__email">neil@mkforvela.com</p>
      <p class="contact__line contact__address">PO BOX 517, Brindlecoe, VIC, 3186</p>
    </div>
  </section>

  <section class="card card--back row-2" aria-label="Card back">
    <div class="partner partner--eyewear">
      <span class="partner__name">VALTIER</span>EYEWEAR
    </div>
    <div class="partner partner--house">
      <span class="partner__square"></span>KELDMANN
    </div>
  </section>

  <section class="card card--front row-2" aria-label="Card front, Priya">
    <div class="brand">
      <div class="brand__tile"></div>
      <span class="brand__name">M&amp;K Forvela</span>
    </div>
    <div class="contact">
      <h2 class="contact__name">Priya Haverstock</h2>
      <p class="contact__line contact__phone">0428650147</p>
      <p class="contact__line contact__email">priya@mkforvela.com</p>
      <p class="contact__line contact__address">PO BOX 517, Brindlecoe, VIC, 3186</p>
    </div>
  </section>

</main>
</body>
</html>
```